Stylish business cards for KX7

To create an appealing and professional business card design for a WOMEN Owned Construction Supply Company.
2 sided card. Incorporate brand elements, curvy, colorful, sleek and bright. No solid white background. attached samples of styles added shapes/ribbons. Want something with that WOW that looks awesome, factor. It is a new logo, so feel free to mess with logo colors in the blue and teal factors that can look good with both dark and light background. If you want to try a watermark with just the KX7, without the "Supply" that might look cool to.

Industry/Entity Type

Women owned construction supply company

Contact Information for Business Card

Name, Title, and phone number and email, web page. maybe spot for qr code.

Font styles to use
Sans Serif

Requirements
Nice to have
• would love to see colors, maybe stylish ribbon dividers or some sort of 2 or 3 tone color card that compliments logo.
Should not have
• Please do not have all white background. Do not include Home/reale state/ or building images.

```html
<!DOCTYPE html>
<html lang="en">
<head>
<meta charset="utf-8">
<title>KX7 Supply – Business Cards</title>
<link rel="stylesheet" href="https://fonts.googleapis.com/css2?family=Montserrat:wght@400;500;600;700&display=swap">
<style>
  :root {
    --backdrop: #3a3a3c;
    --navy: #0f2a4a;
    --navy-deep: #0c2340;
    --teal: #1c95c2;
    --teal-bright: #26a7d6;
    --white: #ffffff;
    --paper: #f1f2f4;
  }
  * { box-sizing: border-box; margin: 0; padding: 0; }
  html, body {
    width: 1200px; height: 1200px; overflow: hidden;
    background: var(--backdrop);
    font-family: "Montserrat", sans-serif;
  }
  .canvas {
    position: relative; width: 1200px; height: 1200px;
  }
  .card {
    position: absolute; left: 220px; width: 760px; height: 434px;
    border-radius: 36px; overflow: hidden;
    box-shadow: 0 3px 0 var(--teal), 0 18px 36px rgba(0,0,0,.45);
  }
  .card--front { top: 150px; }
  .card--back { top: 630px; background: var(--navy); }
  .card__shapes { position: absolute; inset: 0; }

  .brand {
    position: absolute;
    font-weight: 600; letter-spacing: 1px; white-space: nowrap;
    display: flex; align-items: center; gap: 14px;
  }
  .brand__dot { border-radius: 50%; display: inline-block; }
  .card--front .brand {
    left: 430px; top: 160px; font-size: 44px; color: var(--navy);
  }
  .card--front .brand__dot { width: 18px; height: 18px; background: var(--teal); }
  .card--back .brand {
    left: 50%; top: 50%; transform: translate(-50%, -50%);
    font-size: 66px; color: var(--white);
  }
  .card--back .brand__dot { width: 24px; height: 24px; background: var(--teal-bright); }

  .contact {
    position: absolute; left: 56px; top: 232px; color: var(--white);
  }
  .contact__name {
    font-size: 34px; font-weight: 700; color: var(--teal-bright);
    letter-spacing: 1px; line-height: 1;
  }
  .contact__title {
    font-size: 20px; font-weight: 500; letter-spacing: 1px; margin-top: 6px;
  }
  .contact__list { list-style: none; margin-top: 14px; }
  .contact__item {
    display: flex; align-items: center; gap: 12px;
    font-size: 18px; font-weight: 500; letter-spacing: .5px; line-height: 30px;
  }
  .contact__icon { width: 20px; height: 20px; flex: none; }
</style>
</head>
<body>
<main class="canvas">

  <section class="card card--front" aria-label="Card front">
    <svg class="card__shapes" viewBox="0 0 760 434" width="760" height="434" aria-hidden="true">
      <rect width="760" height="434" fill="var(--navy)"/>
      <circle cx="770" cy="-6" r="490" fill="var(--teal)"/>
      <circle cx="770" cy="-6" r="476" fill="var(--white)"/>
      <circle cx="770" cy="-6" r="471" fill="var(--paper)"/>
    </svg>

    <div class="brand"><span class="brand__dot"></span>KX7 Supply</div>

    <div class="contact">
      <p class="contact__name">FULL NAME</p>
      <p class="contact__title">TITLE</p>
      <ul class="contact__list">
        <li class="contact__item">
          <svg class="contact__icon" viewBox="0 0 24 24"><path fill="var(--teal-bright)" d="M6.6 10.8a15 15 0 0 0 6.6 6.6l2.2-2.2c.3-.3.7-.4 1-.2 1.1.4 2.3.6 3.6.6.6 0 1 .4 1 1V20c0 .6-.4 1-1 1A17 17 0 0 1 3 4c0-.6.4-1 1-1h3.5c.6 0 1 .4 1 1 0 1.3.2 2.5.6 3.6.1.3 0 .7-.2 1z"/></svg>
          (000) 000 0000
        </li>
        <li class="contact__item">
          <svg class="contact__icon" viewBox="0 0 24 24"><rect x="2" y="5" width="20" height="14" rx="1" fill="var(--teal-bright)"/><path d="M2 6l10 7 10-7M2 18l7-6M22 18l-7-6" stroke="var(--navy)" stroke-width="1.6" fill="none"/></svg>
          email@company.com
        </li>
        <li class="contact__item">
          <svg class="contact__icon" viewBox="0 0 24 24" fill="none" stroke="var(--teal-bright)" stroke-width="1.8"><circle cx="12" cy="12" r="10"/><ellipse cx="12" cy="12" rx="4.5" ry="10"/><path d="M2 12h20M4 7h16M4 17h16"/></svg>
          www.company.com
        </li>
      </ul>
    </div>
  </section>

  <section class="card card--back" aria-label="Card back">
    <div class="brand"><span class="brand__dot"></span>KX7 Supply</div>
  </section>

</main>
</body>
</html>
```